Waffle Poster Design

Need a A1 size poster (VERTICAL POSTER) to introduce Belgian waffle sandwich. Price is from $6 each. Waffle looks like the attached file. it has different spreads/filling. I found the attached file online, hence the picture quality is not good for an A1 size poster.

```html
<!DOCTYPE html>
<html lang="en">
<head>
<meta charset="utf-8">
<title>Belgian Waffle Sandwich Poster</title>
<link rel="stylesheet" href="https://fonts.googleapis.com/css2?family=Oswald:wght@500;600&family=Montserrat:wght@700&family=Yellowtail&family=Smokum&display=swap">
<style>
  :root {
    --paper: #ffffff;
    --band: #eef2f3;
    --brown: #5a2a0d;
    --red: #c1272d;
    --photo-light: #f3d2a4;
    --photo-deep: #d9a066;
  }
  * { margin: 0; padding: 0; box-sizing: border-box; }
  html, body { width: 1079px; height: 1200px; overflow: hidden; background: var(--paper); }
  .poster { position: relative; width: 1079px; height: 1200px; background: var(--paper); }

  .title-band { position: absolute; left: 32px; top: 28px; width: 1014px; height: 276px; }
  .title-band svg { position: absolute; left: 0; top: 0; }
  .title-script {
    position: absolute; left: 0; right: 0; top: 34px; text-align: center;
    font-family: "Yellowtail", cursive; font-weight: 400; font-size: 140px; line-height: 1;
    color: var(--brown); white-space: nowrap;
  }
  .title-block {
    position: absolute; left: 0; right: 0; top: 160px;
    display: flex; justify-content: center; align-items: center; gap: 22px;
  }
  .title-block .word {
    font-family: "Smokum", serif; font-weight: 400; font-size: 104px; line-height: 1;
    color: var(--red); white-space: nowrap;
  }
  .dots { display: flex; gap: 12px; }
  .dots span { width: 18px; height: 18px; border-radius: 50%; background: var(--red); }

  .price-badge { position: absolute; left: 56px; top: 282px; width: 238px; height: 238px; }
  .price-badge svg { position: absolute; left: 0; top: 0; }
  .price-badge .label {
    position: absolute; inset: 0; display: flex; flex-direction: column;
    align-items: center; justify-content: center; transform: rotate(-8deg);
    font-family: "Oswald", sans-serif; font-weight: 600; line-height: 0.9;
  }
  .price-badge .amount { font-size: 92px; color: var(--red); }
  .price-badge .each { font-size: 46px; color: var(--brown); }

  .menu-heading {
    position: absolute; font-family: "Oswald", sans-serif; font-weight: 600;
    font-size: 64px; line-height: 1; color: var(--brown); text-align: center;
    transform: scaleX(0.9); white-space: nowrap;
  }
  .menu-heading .accent { color: var(--red); }
  .menu-list {
    position: absolute; font-family: "Montserrat", sans-serif; font-weight: 700;
    font-size: 25px; line-height: 30px; color: var(--brown); text-align: center; white-space: nowrap;
  }
  .simply-heading { left: 420px; width: 520px; top: 352px; }
  .simply-list { left: 330px; width: 700px; top: 424px; }
  .combo-heading { left: 180px; width: 600px; top: 552px; }
  .combo-list { left: 40px; width: 1000px; top: 622px; }

  .waffle-photo {
    position: absolute; left: 120px; top: 760px; width: 930px; height: 410px;
    background: linear-gradient(180deg, var(--photo-light) 0%, var(--photo-deep) 100%);
  }
</style>
</head>
<body>
<main class="poster">
  <header class="title-band">
    <svg width="1014" height="276" viewBox="0 0 1014 276" aria-hidden="true">
      <path d="M0 0 H1014 V242 Q507 300 0 242 Z" fill="var(--band)"/>
    </svg>
    <h1 class="title-script">Belgian Waffle</h1>
    <div class="title-block">
      <div class="dots"><span></span><span></span><span></span></div>
      <span class="word">SANDWICH</span>
      <div class="dots"><span></span><span></span><span></span></div>
    </div>
  </header>

  <div class="price-badge">
    <svg width="238" height="238" viewBox="0 0 238 238" aria-hidden="true">
      <circle cx="119" cy="119" r="116" fill="none" stroke="var(--brown)" stroke-width="3"/>
      <circle cx="119" cy="119" r="104" fill="none" stroke="var(--brown)" stroke-width="2.5" stroke-dasharray="2 6" stroke-linecap="round"/>
    </svg>
    <div class="label"><span class="amount">$6</span><span class="each">EACH</span></div>
  </div>

  <h2 class="menu-heading simply-heading">SIMPLY <span class="accent">PERFECT!</span></h2>
  <p class="menu-list simply-list">
    Chocolate • Peanut Butter • Strawberry Coulis<br>
    Choconut • Blueberry • Cream Cheese<br>
    Condensed Milk • Raspberry Couli
  </p>

  <h2 class="menu-heading combo-heading"><span class="accent">PERFECT</span> COMBINATION</h2>
  <p class="menu-list combo-list">
    Ham &amp; Cheddar • Banana Peanu Butter • Banana Chocolate<br>
    Chocolate Peanu Butter • Banana Hazelnut • Ham &amp; Creamcheese<br>
    Blueberry Creamcheese • Strawberry Creamcheese
  </p>

  <div class="waffle-photo" role="img" aria-label="Photo of two golden Belgian waffle sandwiches filled with blueberry spread"></div>
</main>
</body>
</html>
```